Digital Album Cover - Piano music for wedding ceremonies and receptions

I need cover art for a piano album project that will be distributed to TuneVault, Wavelane etc. Covert art required for front of album. At this stage physical CDs will not be printed nor required it is just a digital release.
Artist name: Toby Hargrove
Album Title: Gentle Keys Melodies Wedding Ceremonies and Receptions
Volume 3
Sample piano songs are on my tunecast page
https://tunecast.example/tobyhargrovekeys/sets/gentle-keys-melodies-vol-3
Previous album artwork used from sketch hive competitions winners
https://musicvault.example/au/artist/toby-hargrove/4830917265
Target Market(s)
brides to be
grooms to be
people interested in weddings
people enjoy love songs or easy listening music
Industry/Entity Type
Wedding
Look and feel
Each slider illustrates characteristics of the customer's brand and the style your logo design should communicate.

```html
<!DOCTYPE html>
<html lang="en">
<head>
<meta charset="utf-8">
<title>Toby Hargrove – Gentle Keys Melodies Vol. 3</title>
<link rel="stylesheet" href="https://fonts.googleapis.com/css2?family=Cormorant+Garamond:wght@500&family=Questrial&display=swap">
<style>
  :root {
    --stage: #1c1a19;
    --photo-dark: #2a2826;
    --photo-mid: #5d5650;
    --photo-warm: #d9b58e;
    --photo-light: #c9c2b8;
    --ink: #ffffff;
    --band: rgba(170, 168, 165, 0.42);
  }
  * { margin: 0; padding: 0; box-sizing: border-box; }
  html, body {
    width: 1200px;
    height: 1020px;
    overflow: hidden;
    background: var(--stage);
  }
  .canvas {
    position: relative;
    width: 1200px;
    height: 1020px;
    background: var(--stage);
  }
  .album-cover {
    position: absolute;
    left: 210px;
    top: 120px;
    width: 780px;
    height: 780px;
    overflow: hidden;
  }
  .cover-photo {
    position: absolute;
    inset: 0;
    background:
      radial-gradient(circle at 85% 8%, rgba(230, 190, 140, 0.75) 0%, rgba(200, 160, 120, 0.25) 30%, transparent 55%),
      radial-gradient(ellipse at 62% 78%, var(--photo-light) 0%, rgba(180, 172, 162, 0.4) 22%, transparent 45%),
      linear-gradient(135deg, var(--photo-mid) 0%, var(--photo-dark) 55%, #1f1d1c 100%);
  }
  .cover-text {
    position: absolute;
    inset: 0;
    color: var(--ink);
  }
  .artist-line {
    position: absolute;
    left: 0;
    right: 0;
    top: 138px;
    text-align: center;
    font-family: "Cormorant Garamond", serif;
    font-weight: 500;
    font-size: 27px;
    letter-spacing: 1px;
    text-transform: uppercase;
  }
  .artist-line .divider { margin: 0 8px; }
  .title-word,
  .title-band span {
    font-family: "Questrial", sans-serif;
    text-transform: uppercase;
    white-space: nowrap;
  }
  .title-word {
    position: absolute;
    left: 158px;
    font-size: 60px;
    line-height: 1;
    letter-spacing: 21px;
  }
  .title-band {
    position: absolute;
    left: 129px;
    width: 514px;
    height: 56px;
    background: var(--band);
    display: flex;
    align-items: center;
  }
  .title-band span {
    padding-left: 29px;
    font-size: 32px;
    letter-spacing: 13px;
  }
  .word-gentle { top: 236px; }
  .band-keys { top: 310px; }
  .word-wedding { top: 386px; }
  .band-ceremonies { top: 468px; }
  .word-receptions { top: 541px; letter-spacing: 12px; }
</style>
</head>
<body>
<main class="canvas">
  <section class="album-cover">
    <div class="cover-photo" role="img" aria-label="Soft-focus photograph of a bride holding a bouquet of white tulips and greenery, warm sunlight from the upper right"></div>
    <div class="cover-text">
      <p class="artist-line">Toby Hargrove<span class="divider">|</span>Vol.3</p>
      <h1>
        <span class="title-word word-gentle">Gentle</span>
        <span class="title-band band-keys"><span>Keys Melodies</span></span>
        <span class="title-word word-wedding">Wedding</span>
        <span class="title-band band-ceremonies"><span>Ceremonies &amp;</span></span>
        <span class="title-word word-receptions">Receptions</span>
      </h1>
    </div>
  </section>
</main>
</body>
</html>
```